"You CAN Relax on Your Own Savings!" book cover for 80 page or so book.

Need a book cover that stands out on Bookvale, so highly engaging colors, need to reflect optimism, hope and determination. Go to Bookvale, type my name in and see the covers for the three other books I had written.

There's a lot of negativity and fear for Americans looking at retirement. Yet, they don't need that fear, my book tells them why they can be confident in their ability to retire.

There will be NO spine writing for the book, too small.

Target Market(s)

stressed out people in their 50s and 60s. This book appeals to working people, not high end, wealthy types.

Industry/Entity Type

Financial Planning

Colors

Designer to choose colors to be used in the design.

Requirements
Must have
• Needs to reflect simplicity in action.
• Please spell out my full name, GREG MALTHORPE, at the bottom of the cover.
Nice to have
• if there is anyway to put a picture of an RV (Recreational Vehicle) that would be great.
Should not have
• Do NOT want to be the stodgy, typical financial planning literature out there. No guy in a suit and tie. No one sitting on a beach.
• Do not want my face on the cover either. (On the back yes.)

```html
<!DOCTYPE html>
<html lang="en">
<head>
<meta charset="utf-8">
<title>You CAN Relax on Your Own Savings! — Book Cover</title>
<link rel="stylesheet" href="https://fonts.googleapis.com/css2?family=Alegreya+Sans:wght@500;700;800&family=Marcellus&family=Lato:wght@400;700;900&display=swap">
<style>
  :root {
    --bg: #ececec;
    --paper: #f5f4f0;
    --ink: #3f3f3f;
    --ink-dark: #2a2a2a;
    --red: #c4141c;
    --sky: #dfeef4;
    --lake: #3fb6c8;
    --grass: #7c9a3a;
    --teal: #4aa3a8;
    --rule: #555;
  }
  * { box-sizing: border-box; margin: 0; padding: 0; }
  html, body { width: 1200px; height: 1200px; overflow: hidden; }
  body {
    background: radial-gradient(circle at 50% 40%, #f7f7f7, var(--bg));
    font-family: "Lato", sans-serif;
    color: var(--ink);
    position: relative;
  }
  .cover {
    position: absolute;
    top: 213px;
    width: 500px;
    height: 774px;
    background: var(--paper);
    box-shadow: 0 6px 22px rgba(0,0,0,.14);
    overflow: hidden;
  }
  .cover--front { left: 70px; }
  .cover--back { left: 630px; padding: 38px 36px 0 36px; }

  /* Front */
  .title {
    position: relative;
    z-index: 1;
    text-align: center;
    font-family: "Alegreya Sans", sans-serif;
    font-weight: 800;
    color: var(--ink);
    line-height: 0.98;
    padding-top: 56px;
    letter-spacing: 1px;
  }
  .title__line { display: block; font-size: 72px; }
  .title__sub {
    display: block;
    color: var(--red);
    font-weight: 700;
    font-size: 42px;
    letter-spacing: 0;
    margin-top: 6px;
  }
  .cover__scene {
    position: absolute;
    left: 0; right: 0;
    top: 262px;
    height: 378px;
    background: linear-gradient(180deg, var(--paper) 0%, var(--sky) 10%, #c9e6ee 38%, var(--lake) 58%, #9cc7a0 70%, var(--grass) 82%, #8a7a50 100%);
  }
  .author {
    position: absolute;
    top: 680px; left: 0; right: 0;
    text-align: center;
    font-family: "Marcellus", serif;
    font-size: 35px;
    letter-spacing: 7px;
    color: var(--ink-dark);
  }
  .site {
    position: absolute;
    top: 738px; left: 0; right: 0;
    text-align: center;
    font-size: 16px;
    letter-spacing: 1px;
    color: var(--ink-dark);
  }

  /* Back */
  .quote {
    font-size: 16px;
    line-height: 1.45;
    text-align: center;
    color: var(--ink-dark);
    padding: 0 6px;
  }
  .quote__mark {
    font-family: Georgia, serif;
    font-size: 44px;
    font-weight: 700;
    line-height: 0;
    position: relative;
    top: 14px;
  }
  .bio {
    display: flex;
    gap: 14px;
    margin-top: 34px;
  }
  .bio__text {
    flex: 1;
    text-align: right;
    font-size: 16px;
    line-height: 1.38;
    color: var(--ink-dark);
    padding-right: 12px;
    border-right: 1px solid var(--rule);
  }
  .bio__text p + p { margin-top: 10px; }
  .bio__text strong { font-weight: 900; }
  .bio__portrait {
    width: 170px;
    height: 270px;
    margin-top: 36px;
    background: linear-gradient(180deg, #e8e8e8 0%, #9a9a9a 55%, #6f6f6f 100%);
  }
  .availability {
    margin-top: 28px;
    text-align: center;
    font-size: 15px;
    line-height: 1.45;
    color: var(--ink-dark);
  }
  .availability strong { font-weight: 900; }
  .brand {
    position: absolute;
    left: 0; right: 0;
    bottom: 30px;
    display: flex;
    align-items: center;
    justify-content: center;
    gap: 10px;
    font-family: "Marcellus", serif;
    font-size: 21px;
    letter-spacing: 1px;
    color: var(--teal);
  }
  .brand__dot {
    width: 20px; height: 20px;
    border-radius: 50%;
    background: var(--teal);
  }
</style>
</head>
<body>
  <section class="cover cover--front">
    <div class="cover__scene" role="img" aria-label="A person wrapped in an American flag sits on a rock by a mountain lake, beside a white travel trailer"></div>
    <h1 class="title">
      <span class="title__line">YOU</span>
      <span class="title__line">CAN RELAX</span>
      <span class="title__sub">on Your Own Savings</span>
    </h1>
    <div class="author">GREG MALTHORPE</div>
    <div class="site">www.harborlinewealth.com</div>
  </section>

  <section class="cover cover--back">
    <blockquote class="quote">
      <span class="quote__mark">“</span> is simply dummy text of the printing and typesetting industry. Lorem Ipsum has been the industry's standard dummy text ever since the 1500s, when an unknown printer took a galley of type and scrambled it to make a type specimen book. It has survived not only five centuries, but also the leap into electronic typesetting, remaining essentially unchanged. <span class="quote__mark">”</span>
    </blockquote>

    <div class="bio">
      <div class="bio__text">
        <p>Greg Malthorpe has provided financial advice since 1998 in areas of investment management, Social Security, tax, retirement planning and wealth transfer strategies.</p>
        <p>He has learned that successful financial planning does not need to be complex. He follows the tried and true rule he learned in the Army, <strong>“Keep It Simple, Stupid”</strong></p>
      </div>
      <div class="bio__portrait" role="img" aria-label="Portrait photo of the author in a grey suit"></div>
    </div>

    <p class="availability">
      <strong>YOU CAN RELAX on Your Own Savings</strong> is available at<br>
      www.harborlinewealth.com<br>
      or by emailing greg@harborlinewealth.com
    </p>

    <div class="brand">
      <span class="brand__dot"></span>
      <span>HARBORLINE WEALTH</span>
    </div>
  </section>
</body>
</html>
```